business card for a massage therapy practice named 'Meadow and Willow Massage Studio'

I really need a trendy, yet easy on the eyes business card to complement my logo. Ideally with some gold or rose gold foil work.

My uploaded file of the logo I have in horizontal but I have a vertical version as well. Another color that is used in the website is a blush pink here and there. I'd like to see some trendy tropical leaves in the design.

```html
<!DOCTYPE html>
<html lang="en">
<head>
<meta charset="utf-8">
<title>Meadow and Willow Massage Studio – Business Card</title>
<link href="https://fonts.googleapis.com/css2?family=Montserrat:wght@400;500&family=Arimo:wght@400&display=swap" rel="stylesheet">
<style>
  :root {
    --stage: #000000;
    --sheet: #ffffff;
    --card-edge: #8a8a8a;
    --ink: #1c1c1c;
    --grey: #5d5d5d;
    --gold: #c8952b;
    --gold-name: #e6b41f;
    --blush: #f1c3bd;
    --blush-soft: #f8dcd8;
    --rose-text: #d8968c;
    --leaf-light: #c9dfc6;
    --leaf-deep: #6fae78;
  }
  * { box-sizing: border-box; margin: 0; padding: 0; }
  html, body { width: 1200px; height: 1200px; overflow: hidden; background: var(--stage); }
  .sheet {
    position: absolute; left: 121px; top: 41px; width: 958px; height: 1117px;
    background: var(--sheet);
  }
  .side-label {
    position: absolute; right: 168px; font-family: "Arimo", Arial, sans-serif;
    font-size: 22px; color: var(--ink); letter-spacing: 0.5px;
  }
  .side-label.front-label { top: 57px; }
  .side-label.back-label { top: 604px; }
  .card {
    position: absolute; left: 167px; width: 864px; height: 504px;
    background: var(--sheet); border: 1px solid var(--card-edge); overflow: hidden;
    font-family: "Montserrat", sans-serif;
  }
  .card.front { top: 89px; }
  .card.back { top: 634px; }

  .brand { position: absolute; display: flex; align-items: center; gap: 18px; }
  .brand-dot { width: 70px; height: 70px; border-radius: 50%; background: var(--gold); flex: none; }
  .brand-words { color: var(--ink); font-weight: 400; line-height: 1.1; }
  .brand-name { display: block; font-size: 52px; letter-spacing: 0.5px; }
  .brand-tag { display: block; font-size: 26px; letter-spacing: 6px; text-transform: uppercase; margin-top: 10px; padding-left: 46px; }
  .front .brand { left: 225px; top: 78px; }
  .back .brand { left: 215px; top: 184px; }

  .blush-band { position: absolute; left: 0; width: 100%; background: linear-gradient(90deg, var(--blush) 0%, var(--blush-soft) 70%, var(--blush) 100%); opacity: 0.85; }
  .front .blush-band { top: 243px; height: 52px; }
  .front .blush-trim { position: absolute; left: 169px; right: 0; top: 475px; height: 9px; background: var(--blush); opacity: 0.6; }

  .person { position: absolute; right: calc(864px - 329px); top: 362px; text-align: right; }
  .person-name { font-size: 32px; color: var(--gold-name); font-weight: 400; white-space: nowrap; }
  .person-title { font-size: 24px; color: var(--grey); margin-top: -2px; }
  .gold-rule { position: absolute; left: 402px; top: 339px; width: 9px; height: 108px; background: linear-gradient(180deg, #b67f1f, #e7be55 50%, #b67f1f); }

  .contacts { position: absolute; left: 483px; top: 338px; list-style: none; }
  .contact { display: flex; align-items: center; height: 24px; font-size: 20px; color: var(--ink); }
  .contact + .contact { margin-top: 10px; }
  .contact.social { margin-top: 25px; }
  .contact svg { flex: none; margin-right: 18px; }
  .social-dot { width: 22px; height: 22px; border-radius: 50%; background: var(--gold); margin-right: 12px; flex: none; }

  .leaves { position: absolute; border-radius: 40% 60% 50% 50%; }
  .leaves.top-fronds { left: 137px; top: -20px; width: 544px; height: 130px; background: radial-gradient(ellipse at 60% 20%, var(--leaf-light), rgba(201,223,198,0) 70%); opacity: 0.8; }
  .leaves.side-fronds { left: 633px; top: 94px; width: 208px; height: 408px; background: linear-gradient(200deg, rgba(111,174,120,0.55), rgba(111,174,120,0.15) 80%); }
  .leaves.low-fronds { left: 313px; top: 390px; width: 400px; height: 112px; background: linear-gradient(90deg, rgba(111,174,120,0), rgba(111,174,120,0.45) 60%, rgba(111,174,120,0.2)); }
  .back .blush-band { top: 394px; height: 84px; }
  .web { position: absolute; left: 170px; top: 352px; font-size: 24px; letter-spacing: 11.5px; color: var(--rose-text); white-space: nowrap; }
</style>
</head>
<body>
<main class="sheet" aria-label="Business card layout">
</main>

<span class="side-label front-label">FRONT</span>
<section class="card front" aria-label="Card front">
  <div class="brand">
    <span class="brand-dot"></span>
    <span class="brand-words"><span class="brand-name">Meadow &amp; Willow</span><span class="brand-tag">Massage Studio</span></span>
  </div>
  <div class="blush-band"></div>
  <div class="person">
    <p class="person-name">Marisol Ventura</p>
    <p class="person-title">LMT</p>
  </div>
  <div class="gold-rule"></div>
  <ul class="contacts">
    <li class="contact">
      <svg width="20" height="20" viewBox="0 0 20 20" aria-hidden="true"><rect width="20" height="20" fill="var(--gold)"/><path d="M6 4.5l2.2 2.6-1.2 1.5c.8 1.7 2 2.9 3.6 3.7l1.5-1.2 2.6 2.2-1.4 1.8c-4.3-.6-8-4.3-8.6-8.6z" fill="#fff"/></svg>
      555.214.7380
    </li>
    <li class="contact">
      <svg width="20" height="20" viewBox="0 0 20 20" aria-hidden="true"><rect width="20" height="20" fill="var(--gold)"/><g fill="none" stroke="#fff" stroke-width="1.1"><circle cx="10" cy="10" r="6"/><ellipse cx="10" cy="10" rx="2.6" ry="6"/><path d="M4 10h12M5 7h10M5 13h10"/></g></svg>
      meadowandwillow@mail.com
    </li>
    <li class="contact social">
      <span class="social-dot"></span>@meadowandwillow
    </li>
  </ul>
  <div class="blush-trim"></div>
</section>

<span class="side-label back-label">BACK</span>
<section class="card back" aria-label="Card back">
  <div class="leaves top-fronds" role="img" aria-label="Watercolour palm fronds along the top edge"></div>
  <div class="blush-band"></div>
  <div class="leaves side-fronds" role="img" aria-label="Watercolour tropical leaves curving down the right side"></div>
  <div class="leaves low-fronds" role="img" aria-label="Watercolour palm leaves across the lower edge"></div>
  <div class="brand">
    <span class="brand-dot"></span>
    <span class="brand-words"><span class="brand-name">Meadow &amp; Willow</span><span class="brand-tag">Massage Studio</span></span>
  </div>
  <p class="web">www.meadowandwillow.com</p>
</section>
</body>
</html>
```